Icecream Label Design [Corla Bright]

Our company distributes ice cream in Japan. We produce a private brand that has always been know as Corlas.

However the brand design is poor and we have poor/almost zero brand recognition in the market. Currently people buy our product because it is made in NEW ZEALAND (quality) and represents very good value for money.

BUT

Going forward we want to market Corlas as a 'HIGH QUALITY' icecream BRAND in Japan. We need a package label that reflects this.

We are expanding the current product range (flavour and size) of our Corla's icecream.

I think this is a great opportunity to get your design exposed in a large Asian market. We have very good distribution channels and will will sell a lot of this ice cream in Japan in the future and the Corlas brand/logo will become well recognized.

Really looking forward to seeing design proposals! Thank you, any questions please ask - MTW

Reason: Good morning all. Thank you for submissions. We are wishing to see more examples so have decided to extend the deadline. Looking forward to seeing your ideas. Thanks! Declan

Hi All,

I have sent through the current Corla's logo. Please feel free to use this logo in your designs if you think it is appropriate. There is also an image of the current label for your reference - emphasis on fresh milk but the overall design is not good hence my request to you all...

Looking forward to your help and further submissions. 

Thanks!

Declan 

Reason: Just finalizing design. Have extended deadline to accommodate this. Your continued support and cooperation appreciated. Thanks! Declan

Reason: Finalizing decision being made. Thanks! Declan

Reason: Will make decision today. Thanks all! Declan

Target Market(s)

Mother's 30-55 (quality ingredients and value for money)

Industry/Entity Type

It Company

Requirements
Must have
• 1. The brand is Corla Bright

2. You are designing a logo that will be used on our 1 litre tub and 500ML pottle. Design specification files are attached*.
*Please note: on both the 1L and 500ML tub space must be left for regulatory information. Image attached showing current regulatory information and and space on the 1L tub.

3. We want to use this logo/branding as a base for all our 4 flavour varieties noted below so the design must be able to accommodate this somehow.

4. Needs to have a text placeholder for Japanese translation. ie: if on the design you use text that says 'Vanilla Ice Cream' then somewhere there needs to be space for the Japanese equivalent バニラ アイスクリーム
Nice to have
• 1. Corlas uses 100% fresh milk and cream. It would be nice to convey this somehow.

2. Perhaps could include text 'Your Fresh Taste of New Zealand'

3. There are 4* flavour varieties.
Vanilla | Strawberry | Chocolate | Green Tea
* it would be nice to have a good Corlas base design/pattern which can then be modified slightly (image, colour etc maybe) to reflect each unique flavour.

```html
<!DOCTYPE html>
<html lang="en">
<head>
<meta charset="utf-8">
<title>Corla's High Quality Ice Cream – Label Range</title>
<link rel="stylesheet" href="https://fonts.googleapis.com/css2?family=Open+Sans:wght@400;600;700&family=Noto+Sans+JP:wght@400;500&display=swap">
<style>
  :root {
    --canvas: #f1f1f2;
    --silver-light: #f7f7f8;
    --silver-mid: #d9dadc;
    --silver-dark: #b9bbbe;
    --vanilla: #2e3190;
    --chocolate: #7b1f1d;
    --strawberry: #e5186a;
    --green-tea: #7dc243;
    --seal-black: #1e1e1e;
    --white: #ffffff;
    --milk: #ffffff;
    --art-vanilla: #f3e3a6;
    --art-chocolate: #9a8a86;
    --art-strawberry: #f04a57;
    --art-green-tea: #5aa845;
  }

  * { box-sizing: border-box; margin: 0; padding: 0; }

  html, body {
    width: 1200px;
    height: 604px;
    overflow: hidden;
    background: var(--canvas);
    font-family: "Open Sans", Arial, sans-serif;
  }

  .range { position: relative; width: 1200px; height: 604px; }

  .shape-defs { position: absolute; width: 0; height: 0; }

  /* ---------- shared silver surfaces ---------- */
  .wrap-label,
  .lid-label {
    position: absolute;
    overflow: hidden;
    color: var(--flavour);
  }

  .wrap-label {
    background: linear-gradient(90deg,
      var(--silver-dark) 0%, var(--silver-light) 22%,
      var(--silver-mid) 48%, var(--silver-light) 72%, var(--silver-dark) 100%);
  }

  .lid-label {
    border-radius: 50%;
    background: radial-gradient(circle at 40% 35%,
      var(--silver-light) 0%, var(--silver-mid) 70%, var(--silver-dark) 100%);
  }

  /* ---------- scalloped flavour seal ---------- */
  .seal {
    position: absolute;
    width: var(--s);
    height: var(--s);
    font-size: calc(var(--s) / 10);
    color: var(--white);
    text-align: center;
    --flavour-size: 0.4em;
    --jp-size: 0.34em;
  }

  .seal-shape {
    position: absolute;
    inset: 0;
    width: 100%;
    height: 100%;
    color: var(--flavour);
  }

  .seal-flavour,
  .seal-brand,
  .seal-tagline,
  .seal-jp {
    position: absolute;
    left: 0;
    width: 100%;
    line-height: 1;
    white-space: nowrap;
  }

  .seal-flavour { top: 20%; font-size: var(--flavour-size); font-weight: 600; }
  .seal-brand   { top: 28%; font-size: 2em; font-weight: 700; letter-spacing: -0.02em; }
  .seal-tagline { top: 51%; font-size: 0.62em; font-weight: 400; }
  .seal-tagline strong { font-weight: 700; }
  .seal-jp {
    top: 73%;
    font-family: "Noto Sans JP", "Open Sans", sans-serif;
    font-size: var(--jp-size);
    font-weight: 500;
  }

  .seal-art {
    position: absolute;
    top: 59%;
    left: 32%;
    width: 36%;
    height: 12%;
    border-radius: 0.6em;
    background: radial-gradient(ellipse at center, var(--art) 0%, var(--art) 45%, transparent 72%);
  }

  /* ---------- origin seal (plain shape) ---------- */
  .origin-seal {
    position: absolute;
    width: var(--o);
    height: var(--o);
    border-radius: 50%;
    background: var(--seal-black);
    border: 2px solid var(--white);
  }

  /* ---------- milk splash area ---------- */
  .milk-splash {
    position: absolute;
    left: 0;
    width: 100%;
    background:
      radial-gradient(ellipse 60% 55% at 30% 70%, var(--milk) 0%, rgba(255,255,255,0.85) 40%, transparent 75%),
      radial-gradient(ellipse 55% 50% at 75% 80%, var(--milk) 0%, rgba(214,228,238,0.7) 45%, transparent 78%);
  }

  /* ---------- fresh milk claim ---------- */
  .milk-claim {
    position: absolute;
    color: var(--flavour);
    line-height: 1.05;
    font-weight: 700;
    white-space: nowrap;
  }
  .milk-claim .claim-percent { font-size: 1.45em; }
  .milk-claim .claim-line { display: block; }

  /* ---------- flavours ---------- */
  .flavour-vanilla    { --flavour: var(--vanilla);    --art: var(--art-vanilla); }
  .flavour-chocolate  { --flavour: var(--chocolate);  --art: var(--art-chocolate); }
  .flavour-strawberry { --flavour: var(--strawberry); --art: var(--art-strawberry); }
  .flavour-green-tea  { --flavour: var(--green-tea);  --art: var(--art-green-tea); }

  /* ---------- placements ---------- */
  .wrap-label--large { left: 305px; top: 75px; width: 340px; height: 500px; }
  .wrap-label--large .seal { --s: 262px; --flavour-size: 0.5em; --jp-size: 0.48em; left: 30px; top: 112px; }
  .wrap-label--large .origin-seal { --o: 96px; left: 236px; top: 28px; }
  .wrap-label--large .milk-splash { top: 360px; height: 140px; }
  .wrap-label--large .milk-claim { left: 26px; top: 430px; font-size: 15px; }

  .wrap-label--small { top: 292px; width: 200px; height: 292px; }
  .wrap-label--small .seal { --s: 156px; left: 16px; top: 66px; }
  .wrap-label--small .origin-seal { --o: 56px; left: 138px; top: 14px; }
  .wrap-label--small .milk-splash { top: 204px; height: 88px; }
  .wrap-label--small .milk-claim { left: 16px; top: 240px; font-size: 10px; }

  .wrap-label--chocolate  { left: 25px; }
  .wrap-label--strawberry { left: 715px; }
  .wrap-label--green-tea  { left: 968px; }

  .lid-label { top: 8px; width: 216px; height: 216px; }
  .lid-label .seal { --s: 146px; left: 12px; top: 14px; }
  .lid-label .origin-seal { --o: 50px; left: 160px; top: 60px; }
  .lid-label .milk-splash { top: 140px; height: 76px; }
  .lid-label .milk-claim { left: 44px; top: 168px; font-size: 9px; }

  .lid-label--chocolate { left: 8px; }
  .lid-label--vanilla   { left: 702px; }
  .lid-label--green-tea { left: 948px; }
</style>
</head>
<body>
<main class="range">

  <svg class="shape-defs" aria-hidden="true" focusable="false">
    <defs>
      <polygon id="seal-outline" points="100,0 91.2,12 96.6,25.9 85,35.2 86.6,50 73,56 70.7,70.7 56,73 50,86.6 35.2,85 25.9,96.6 12,91.2 0,100 -12,91.2 -25.9,96.6 -35.2,85 -50,86.6 -56,73 -70.7,70.7 -73,56 -86.6,50 -85,35.2 -96.6,25.9 -91.2,12 -100,0 -91.2,-12 -96.6,-25.9 -85,-35.2 -86.6,-50 -73,-56 -70.7,-70.7 -56,-73 -50,-86.6 -35.2,-85 -25.9,-96.6 -12,-91.2 0,-100 12,-91.2 25.9,-96.6 35.2,-85 50,-86.6 56,-73 70.7,-70.7 73,-56 86.6,-50 85,-35.2 96.6,-25.9 91.2,-12"/>
    </defs>
  </svg>

  <!-- Lids -->
  <section class="lid-label lid-label--chocolate flavour-chocolate" aria-label="Chocolate lid label">
    <div class="milk-splash" role="img" aria-label="Splash of fresh milk"></div>
    <div class="seal">
      <svg class="seal-shape" viewBox="-100 -100 200 200" aria-hidden="true"><use href="#seal-outline" fill="currentColor"/><circle r="80" fill="none" stroke="#fff" stroke-width="1.2" opacity=".6"/></svg>
      <p class="seal-flavour">Chocolate Ice Cream - 500mL</p>
      <p class="seal-brand">Corla's</p>
      <p class="seal-tagline"><strong>High Quality</strong> Ice Cream</p>
      <div class="seal-art" role="img" aria-label="Chocolate pieces"></div>
      <p class="seal-jp" lang="ja">チョコレートアイスクリーム - 500mL</p>
    </div>
    <div class="origin-seal" aria-hidden="true"></div>
    <p class="milk-claim"><span class="claim-line">Corla's uses <span class="claim-percent">100%</span></span><span class="claim-line">fresh milk &amp; cream</span></p>
  </section>

  <section class="lid-label lid-label--vanilla flavour-vanilla" aria-label="Vanilla lid label">
    <div class="milk-splash" role="img" aria-label="Splash of fresh milk"></div>
    <div class="seal">
      <svg class="seal-shape" viewBox="-100 -100 200 200" aria-hidden="true"><use href="#seal-outline" fill="currentColor"/><circle r="80" fill="none" stroke="#fff" stroke-width="1.2" opacity=".6"/></svg>
      <p class="seal-flavour">Vanilla Ice Cream - 500mL</p>
      <p class="seal-brand">Corla's</p>
      <p class="seal-tagline"><strong>High Quality</strong> Ice Cream</p>
      <div class="seal-art" role="img" aria-label="Vanilla flower and pods"></div>
      <p class="seal-jp" lang="ja">バニラ アイスクリーム - 500mL</p>
    </div>
    <div class="origin-seal" aria-hidden="true"></div>
    <p class="milk-claim"><span class="claim-line">Corla's uses <span class="claim-percent">100%</span></span><span class="claim-line">fresh milk &amp; cream</span></p>
  </section>

  <section class="lid-label lid-label--green-tea flavour-green-tea" aria-label="Green tea lid label">
    <div class="milk-splash" role="img" aria-label="Splash of fresh milk"></div>
    <div class="seal">
      <svg class="seal-shape" viewBox="-100 -100 200 200" aria-hidden="true"><use href="#seal-outline" fill="currentColor"/><circle r="80" fill="none" stroke="#fff" stroke-width="1.2" opacity=".6"/></svg>
      <p class="seal-flavour">Green Tea Ice Cream - 500mL</p>
      <p class="seal-brand">Corla's</p>
      <p class="seal-tagline"><strong>High Quality</strong> Ice Cream</p>
      <div class="seal-art" role="img" aria-label="Green tea leaves"></div>
      <p class="seal-jp" lang="ja">抹茶 アイスクリーム - 500mL</p>
    </div>
    <div class="origin-seal" aria-hidden="true"></div>
    <p class="milk-claim"><span class="claim-line">Corla's uses <span class="claim-percent">100%</span></span><span class="claim-line">fresh milk &amp; cream</span></p>
  </section>

  <!-- Wrap labels -->
  <section class="wrap-label wrap-label--small wrap-label--chocolate flavour-chocolate" aria-label="Chocolate tub label">
    <div class="milk-splash" role="img" aria-label="Splash of fresh milk"></div>
    <div class="seal">
      <svg class="seal-shape" viewBox="-100 -100 200 200" aria-hidden="true"><use href="#seal-outline" fill="currentColor"/><circle r="80" fill="none" stroke="#fff" stroke-width="1.2" opacity=".6"/></svg>
      <p class="seal-flavour">Chocolate Ice Cream - 500mL</p>
      <p class="seal-brand">Corla's</p>
      <p class="seal-tagline"><strong>High Quality</strong> Ice Cream</p>
      <div class="seal-art" role="img" aria-label="Chocolate pieces"></div>
      <p class="seal-jp" lang="ja">チョコレートアイスクリーム - 500mL</p>
    </div>
    <div class="origin-seal" aria-hidden="true"></div>
    <p class="milk-claim"><span class="claim-line">Corla's uses <span class="claim-percent">100%</span></span><span class="claim-line">fresh milk &amp; cream</span></p>
  </section>

  <section class="wrap-label wrap-label--large flavour-vanilla" aria-label="Vanilla tub label">
    <div class="milk-splash" role="img" aria-label="Splash of fresh milk"></div>
    <div class="seal">
      <svg class="seal-shape" viewBox="-100 -100 200 200" aria-hidden="true"><use href="#seal-outline" fill="currentColor"/><circle r="80" fill="none" stroke="#fff" stroke-width="1.2" opacity=".6"/></svg>
      <p class="seal-flavour">Vanilla Icecream - 500mL</p>
      <p class="seal-brand">Corla's</p>
      <p class="seal-tagline"><strong>High Quality</strong> Ice Cream</p>
      <div class="seal-art" role="img" aria-label="Vanilla flower and pods"></div>
      <p class="seal-jp" lang="ja">バニラ アイスクリーム - 500mL</p>
    </div>
    <div class="origin-seal" aria-hidden="true"></div>
    <p class="milk-claim"><span class="claim-line">Corla's uses <span class="claim-percent">100%</span></span><span class="claim-line">fresh milk &amp; cream</span></p>
  </section>

  <section class="wrap-label wrap-label--small wrap-label--strawberry flavour-strawberry" aria-label="Strawberry tub label">
    <div class="milk-splash" role="img" aria-label="Splash of fresh milk"></div>
    <div class="seal">
      <svg class="seal-shape" viewBox="-100 -100 200 200" aria-hidden="true"><use href="#seal-outline" fill="currentColor"/><circle r="80" fill="none" stroke="#fff" stroke-width="1.2" opacity=".6"/></svg>
      <p class="seal-flavour">Strawberry Ice Cream - 500mL</p>
      <p class="seal-brand">Corla's</p>
      <p class="seal-tagline"><strong>High Quality</strong> Ice Cream</p>
      <div class="seal-art" role="img" aria-label="Fresh strawberry"></div>
      <p class="seal-jp" lang="ja">ストロベリーアイスクリーム - 500mL</p>
    </div>
    <div class="origin-seal" aria-hidden="true"></div>
    <p class="milk-claim"><span class="claim-line">Corla's uses <span class="claim-percent">100%</span></span><span class="claim-line">fresh milk &amp; cream</span></p>
  </section>

  <section class="wrap-label wrap-label--small wrap-label--green-tea flavour-green-tea" aria-label="Green tea tub label">
    <div class="milk-splash" role="img" aria-label="Splash of fresh milk"></div>
    <div class="seal">
      <svg class="seal-shape" viewBox="-100 -100 200 200" aria-hidden="true"><use href="#seal-outline" fill="currentColor"/><circle r="80" fill="none" stroke="#fff" stroke-width="1.2" opacity=".6"/></svg>
      <p class="seal-flavour">Green Tea Ice Cream - 500mL</p>
      <p class="seal-brand">Corla's</p>
      <p class="seal-tagline"><strong>High Quality</strong> Ice Cream</p>
      <div class="seal-art" role="img" aria-label="Green tea leaves"></div>
      <p class="seal-jp" lang="ja">抹茶 アイスクリーム - 500mL</p>
    </div>
    <div class="origin-seal" aria-hidden="true"></div>
    <p class="milk-claim"><span class="claim-line">Corla's uses <span class="claim-percent">100%</span></span><span class="claim-line">fresh milk &amp; cream</span></p>
  </section>

</main>
</body>
</html>
```